Byte Lantern Website

Design and implement (fully coded and ready to launch) website for a professional services company - please see the documents attached and send us an email if there are any questions
Target Market(s)
Market to potential clients about the services we offer and be able to reach us for any consulting opportunities
Industry/Entity Type
Professional Service
Coding
Coded - Design and coding required
Number of Pages Required
3 page
Requirements
Must have
- Single page website design that is SEO optimized
Blog Post
Contact US page
Cool images/ logos for the service offering - not fill the website with text/content
Must be professional looking website
Coded website should also look great on different screens - mobile, tablets etc
Nice to have
- Choose easy neutral colors that compliment the logo colors. Having said that don't use every color in the logo for the website design.
Should not have
- Too many colors and several various different fonts

```html
<!DOCTYPE html>
<html lang="en">
<head>
<meta charset="utf-8">
<title>Byte Lantern LLC</title>
<link href="https://fonts.googleapis.com/css2?family=Roboto+Slab:wght@400;500;700&family=Open+Sans:wght@400;600&display=swap" rel="stylesheet">
<style>
:root{
  --orange:#f26522;
  --navy:#1f2a44;
  --blue:#1a5aa8;
  --accent:#2a62c0;
  --indigo:#3d4f9c;
  --ink:#222;
  --muted:#6b6b6b;
  --panel:#f4f4f4;
  --line:#d8d8d8;
  --footer:#1c1c1c;
}
*{margin:0;padding:0;box-sizing:border-box}
html,body{width:1200px;height:5367px;overflow:hidden;background:#fff}
body{font-family:"Open Sans",sans-serif;color:var(--ink);position:relative}
.slab{font-family:"Roboto Slab",serif}
.abs{position:absolute}
section,header,footer{position:absolute;left:0;width:1200px}
.btn{position:absolute;background:var(--orange);color:#fff;font-family:"Roboto Slab",serif;font-weight:700;font-size:17px;display:flex;align-items:center;justify-content:center;letter-spacing:.5px;border-radius:2px}
.link-more{position:absolute;color:var(--orange);text-decoration:underline;font-family:"Roboto Slab",serif;font-size:17px}

/* header */
.site-header{top:0;height:133px}
.brand{position:absolute;left:88px;top:40px;display:flex;align-items:center;gap:12px;font-family:"Roboto Slab",serif;font-weight:700;font-size:28px;color:var(--navy)}
.brand-dot{width:26px;height:26px;border-radius:50%;background:var(--orange)}
.nav{position:absolute;left:423px;top:84px;display:flex;gap:24px;font-family:"Roboto Slab",serif;font-size:14px;font-weight:500;color:var(--ink)}
.nav .active{color:var(--orange);text-decoration:underline}
.social{position:absolute;top:18px;left:982px;display:flex;gap:6px}
.social span{width:40px;height:40px;border-radius:50%;background:var(--blue);display:block}

/* hero */
.hero{top:133px;height:584px;background:linear-gradient(180deg,#2c3f5c 0%,#3a5478 45%,#6a86a8 80%,#4a6283 100%)}
.hero-title{left:88px;top:210px;font-size:52px;font-weight:700;color:#fff}
.hero-rule{left:88px;top:289px;width:80px;height:2px;background:#fff}
.hero-text{left:177px;top:278px;width:420px;font-size:15.5px;line-height:24px;color:#fff}

/* expertise */
.section-title{position:absolute;left:0;width:1200px;text-align:center;font-family:"Roboto Slab",serif;font-weight:700;font-size:34px;color:var(--ink)}
.section-title em{font-style:normal;color:var(--accent)}
.expertise{top:717px;height:901px}
.expertise .sub{position:absolute;top:150px;width:1200px;text-align:center;font-size:16px;color:var(--muted)}
.tech-grid{position:absolute;left:146px;top:210px;width:854px;height:490px;display:grid;grid-template-columns:283px 286px 285px;grid-template-rows:242px 248px}
.tech{display:flex;flex-direction:column;align-items:center;text-align:center}
.tech:nth-child(-n+3){border-bottom:1px solid var(--line)}
.tech:nth-child(3n+1),.tech:nth-child(3n+2){border-right:1px solid var(--line)}
.tech-name{margin-top:82px;height:40px;display:flex;align-items:center;font-family:"Roboto Slab",serif;font-weight:700;font-size:26px;color:var(--navy)}
.tech-label{margin-top:26px;font-family:"Roboto Slab",serif;font-weight:500;font-size:20px;line-height:32px;color:var(--blue)}

/* profile */
.profile{top:1618px;height:555px;background:var(--blue)}
.profile-photo{left:0;top:0;width:510px;height:555px;background:linear-gradient(135deg,#c9c3b8,#8c8378 50%,#d8d2c6)}
.profile h2{position:absolute;left:558px;top:100px;font-family:"Roboto Slab",serif;font-weight:500;font-size:34px;color:#fff;letter-spacing:.5px}
.profile p{position:absolute;left:560px;top:166px;width:550px;font-size:15.5px;line-height:29px;color:#fff;text-align:justify}

/* services */
.services{top:2173px;height:1549px}
.svc-photo{position:absolute;width:520px;height:360px}
.svc-card{position:absolute;background:var(--panel);padding:46px 44px 0 44px}
.svc-card h3{font-family:"Roboto Slab",serif;font-weight:700;font-size:27px;color:var(--ink)}
.svc-card p{margin-top:16px;font-size:13.5px;line-height:28px;color:var(--muted);text-align:justify}

/* founder */
.founder{top:3722px;height:523px;background:var(--indigo)}
.founder-photo{left:637px;top:0;width:563px;height:523px;background:linear-gradient(160deg,#6b4a35,#a67b5b 50%,#7d5c46)}
.founder h2{position:absolute;left:90px;top:120px;font-family:"Roboto Slab",serif;font-weight:400;font-size:24px;color:#fff}
.founder p{position:absolute;left:88px;top:176px;width:452px;font-size:15.5px;line-height:27.5px;color:#fff;text-align:justify}

/* blog */
.blog{top:4245px;height:704px}
.post{position:absolute;top:200px;width:328px;height:413px;background:#fff;box-shadow:0 2px 8px rgba(0,0,0,.15)}
.post-img{height:205px}
.post h3{margin:18px 0 0 14px;font-family:"Roboto Slab",serif;font-weight:700;font-size:21px}
.post time{display:block;margin:6px 0 0 14px;font-size:12px;color:var(--muted)}
.post p{margin:8px 14px 0;font-size:12.5px;line-height:27px;color:var(--muted);text-align:justify}

/* footer */
.site-footer{top:4949px;height:418px;background:var(--footer);color:#fff}
.fcol{position:absolute;top:72px}
.fcol h4{font-family:"Roboto Slab",serif;font-weight:700;font-size:18px}
.fcol ul{list-style:none;margin-top:26px}
.fcol li{font-size:15px;line-height:34px}
.field{position:absolute;left:883px;width:225px;height:42px;border:1px solid #9a9a9a;font-size:11px;padding:0 8px;display:flex;align-items:center}
.copyright{position:absolute;top:358px;width:1200px;text-align:center;font-family:"Roboto Slab",serif;font-size:16px}
</style>
</head>
<body>

<header class="site-header">
  <div class="brand"><span class="brand-dot"></span>BYTE LANTERN</div>
  <nav class="nav">
    <span class="active">HOME</span><span>ABOUT US</span><span>SERVICES</span><span>TECHNOLOGY EXPERTISE</span><span>TEAM</span><span>BLOG</span><span>CONTACT US</span>
  </nav>
  <div class="social" aria-label="Social links"><span></span><span></span><span></span></div>
</header>

<section class="hero" role="img" aria-label="Businessman on a rooftop overlooking a city skyline at dusk with network lines">
  <h1 class="abs hero-title slab">BYTE LANTERN LLC.</h1>
  <div class="abs hero-rule"></div>
  <p class="abs hero-text">Lorem ipsum dolor sit amet, consectetur adipiscing elit, sed do eiusmod tempor incididunt ut labore</p>
  <a class="btn" style="left:177px;top:344px;width:148px;height:40px">GET STARTED</a>
</section>

<section class="expertise">
  <h2 class="section-title" style="top:94px">OUR TECHNOLOGY <em>EXPERTISE</em></h2>
  <p class="sub">Lorem ipsum dolor sit amet, consectetur adipiscing elit, sed do eiusmod tempor incididunt ut</p>
  <div class="tech-grid">
    <div class="tech"><div class="tech-name">Cloudmere</div><div class="tech-label">CLOUDMERE DATA<br>PLATFORM</div></div>
    <div class="tech"><div class="tech-name">Ember Stream</div><div class="tech-label">EMBER<br>STREAM</div></div>
    <div class="tech"><div class="tech-name">Frostgrid</div><div class="tech-label">FROST<br>GRID</div></div>
    <div class="tech"><div class="tech-name" style="margin-top:64px">Nimbus</div><div class="tech-label" style="margin-top:44px">NIMBUS WEB<br>SERVICES</div></div>
    <div class="tech"><div class="tech-name" style="margin-top:64px">Flowlink</div><div class="tech-label" style="margin-top:44px">FLOW<br>LINK</div></div>
    <div class="tech"><div class="tech-name" style="margin-top:64px">Relaybus</div><div class="tech-label" style="margin-top:44px">RELAY<br>BUS</div></div>
  </div>
  <a class="btn" style="left:525px;top:756px;width:150px;height:40px">VIEW MORE</a>
</section>

<section class="profile">
  <div class="abs profile-photo" role="img" aria-label="Three colleagues working together at a laptop"></div>
  <h2>COMPANY&nbsp; PROFILE</h2>
  <p>Byte Lantern provides end to end services in architecture, design and development of DataPlatforms, Analytic workloads, Data Engineering, Cloud Engineering Byte Lantern is a company which intends to be in front of the client's needs, deeply understanding clients' business and delivering and optimizing solutions from the initial phase of scoping the requirements, up to the final delivery, maintenance and continuous upgrade</p>
  <a class="btn" style="left:560px;top:403px;width:150px;height:43px">READ MORE</a>
</section>

<section class="services">
  <h2 class="section-title" style="top:96px">OUR <em>SERVICES</em></h2>

  <div class="svc-photo" style="left:90px;top:204px;background:linear-gradient(180deg,#14161c,#3a3f4a 50%,#c99a4c 70%,#111)" role="img" aria-label="Laptop with a glowing city rising from the screen"></div>
  <div class="svc-card" style="left:521px;top:221px;width:589px;height:324px">
    <h3>PLATFORM ARCHITECTURE</h3>
    <p>Byte Lantern works very closely with clients, product managers to understand the scope of the requirements, discuss myriad of technologies choices available both on on-premise,cloud-native services, storage formats, data governance, ingestions, migration, CI/CD,system integrations and serving layer making the data available to their customers meeting.</p>
  </div>
  <a class="link-more" style="left:569px;top:494px">READ MORE</a>

  <div class="svc-photo" style="left:587px;top:629px;width:523px;background:linear-gradient(135deg,#cfe3ef,#eef5fa 50%,#9fc0d6)" role="img" aria-label="Man facing a wall of data network diagrams"></div>
  <div class="svc-card" style="left:90px;top:650px;width:587px;height:322px;z-index:1">
    <h3>DATA ENGINEERING</h3>
    <p>Byte Lantern employs the latest proven technologies, best practices, industry standards in building the Data Lakes that has become the business standard in any Industry, or any size of Company to utilize the data it has about its customers, inventory or sales or social mediaposting, feedback, using the data to gain business insights on a near-real time basis to</p>
  </div>
  <a class="link-more" style="left:137px;top:921px;z-index:2">READ MORE</a>

  <div class="svc-photo" style="left:90px;top:1083px;background:linear-gradient(135deg,#101a3a,#2a3f8c 40%,#d68a3a 75%,#5a2a1a)" role="img" aria-label="Glowing cloud over a circuit board"></div>
  <div class="svc-card" style="left:521px;top:1099px;width:589px;height:323px">
    <h3>CLOUD DEVELOPMENTS</h3>
    <p>Lorem ipsum dolor sit amet, consectetur adipiscing elit, sed do eiusmod tempor incididunt ut labore et dolore magna aliqua. Ut enim ad minim veniam, quis nostrud exercitation ullamco laboris nisi ut aliquip ex ea commodo consequat. Duis aute irure dolor in reprehenderit in voluptate velit esse cillum dolore eu fugiat nulla pariatur. Excepteur sint occaecat cupidatat non proident, sunt in culpa qui officia deserunt</p>
  </div>
  <a class="link-more" style="left:569px;top:1372px">READ MORE</a>
</section>

<section class="founder">
  <div class="abs founder-photo" role="img" aria-label="Portrait of the founder"></div>
  <h2>RAVI MENON – FOUNDER</h2>
  <p>Ravi manages all the client interactions and engineering team at Byte Lantern. Ravi has over15 years of experience in the technology before he founded Byte Lantern. He managed development of large scale enterprise wide, high performance, scalable, real-time software solutions in Tele-communications, Gaming, Finance, and Insurance Industries.</p>
  <a class="btn" style="left:94px;top:392px;width:150px;height:42px">READ MORE</a>
</section>

<section class="blog">
  <h2 class="section-title" style="top:100px">LASTEST <em>BLOG</em></h2>
  <article class="post" style="left:90px">
    <div class="post-img" style="background:linear-gradient(135deg,#0f1f3d,#2f5a8f 60%,#18243a)" role="img" aria-label="Analysts working at monitors in a control room"></div>
    <h3>LOREM IPSUM</h3><time>JAN 23,2020</time>
    <p>Lorem ipsum dolor sit amet, consectetur adipiscing elit, sed do eiusmod tempor incididunt ut labore et dolore magna aliqua. Ut enim ad minim veniam, quis nostrud exercitation</p>
  </article>
  <article class="post" style="left:435px">
    <div class="post-img" style="background:linear-gradient(135deg,#dfe3e6,#9aa4ab 60%,#c8ced2)" role="img" aria-label="Team meeting in a bright office"></div>
    <h3>LOREM IPSUM</h3><time>JAN 22,2020</time>
    <p>Lorem ipsum dolor sit amet, consectetur adipiscing elit, sed do eiusmod tempor incididunt ut labore et dolore magna aliqua. Ut enim ad minim veniam, quis nostrud exercitation</p>
  </article>
  <article class="post" style="left:781px">
    <div class="post-img" style="background:linear-gradient(135deg,#2c4a66,#8fb0c8 55%,#3a5670)" role="img" aria-label="Year numbers over a city with network lines"></div>
    <h3>LOREM IPSUM</h3><time>JAN 20,2020</time>
    <p>Lorem ipsum dolor sit amet, consectetur adipiscing elit, sed do eiusmod tempor incididunt ut labore et dolore magna aliqua. Ut enim ad minim veniam, quis nostrud exercitation</p>
  </article>
</section>

<footer class="site-footer">
  <div class="fcol" style="left:90px"><h4>QUICKS LINKS</h4>
    <ul><li>Home</li><li>About Us</li><li>Services</li><li>Technology Expertise</li><li>Team</li><li>Blog</li><li>Contact Us</li></ul></div>
  <div class="fcol" style="left:333px"><h4>SERVICES</h4>
    <ul><li>Platform Architecture</li><li>Data Engineering</li><li>Cloud Developments</li></ul></div>
  <div class="fcol" style="left:585px"><h4>CONTACT US</h4>
    <ul><li>18 Alder Row</li><li>Milbrook, North Carolina</li><li>555 014 2290</li><li>info@bytelantern.com</li></ul></div>
  <div class="fcol" style="left:887px"><h4>MESSAGE US</h4></div>
  <div class="field" style="top:132px">NAME</div>
  <div class="field" style="top:182px">EMAIL</div>
  <div class="field" style="top:234px">MESSAGE</div>
  <a class="btn" style="left:994px;top:298px;width:114px;height:36px;font-size:14px">SUBMIT</a>
  <p class="copyright">© Copyright 2020 Byte Lantern LLC.. All Rights Reserved</p>
</footer>

</body>
</html>
```